Accounting Practice Business Card Design

I have a logo I am happy for you to use in the design of the Business Card.
You can edit and change colours as you please, I am not fixated on it.
I am looking for a modern and clean overall feel for the finished design.

The business is a small accounting practice who thrives on word of mouth referrals and this card will be given to all current and prospect clients.

Industry/Entity Type

Accountant

Contact Information for Business Card

Marcus Elwin
Level 5, 8 Corvale Ridge Road
ASHGROVE RISE VIC 3187
Phone: 9481 3057
Email: melwin@mrfaccountants.com.au
Web: www.mrfaccountants.com.au

Font styles to use
Serif
Sans Serif

Colors
0555a3
3277b5
85acd3
0393ce
33a6d7
85cae6
00a990
33b8a4
9bcb3c

Requirements
Must have
• "The end to your tax problems begin with us"
• "A referral from you is our greatest compliment"
Nice to have
• Modern clean professional

```html
<!DOCTYPE html>
<html lang="en">
<head>
<meta charset="utf-8">
<title>MRF Accountants – Business Card</title>
<link rel="stylesheet" href="https://fonts.googleapis.com/css2?family=Heebo:wght@400;700;800&display=swap">
<style>
  :root {
    --navy: #13467a;
    --navy-text: #0e3f78;
    --grey-text: #555a60;
    --rule: #5a5a5a;
    --card-white: #ffffff;
    --backdrop: #2e2f31;
    --on-navy: #ffffff;
  }
  * { margin: 0; padding: 0; box-sizing: border-box; }
  html, body {
    width: 1200px;
    height: 960px;
    overflow: hidden;
    background: var(--backdrop);
    font-family: "Heebo", "Helvetica Neue", Arial, sans-serif;
  }
  .canvas { position: relative; width: 1200px; height: 960px; }

  .card {
    position: absolute;
    left: 281px;
    width: 655px;
    height: 374px;
    border-radius: 18px;
    overflow: hidden;
  }
  .card--front { top: 80px; background: var(--card-white); }
  .card--back  { top: 506px; background: var(--navy); }

  .brand-name {
    position: absolute;
    right: 42px;
    font-weight: 800;
    font-size: 30px;
    line-height: 1;
    letter-spacing: 0.5px;
    text-align: right;
  }
  .card--front .brand-name { top: 58px; color: var(--navy-text); }
  .card--back  .brand-name { top: 62px; color: var(--on-navy); }

  .tagline {
    position: absolute;
    right: 42px;
    top: 125px;
    font-size: 15px;
    color: var(--grey-text);
  }

  .person { position: absolute; left: 48px; top: 180px; }
  .person__name { font-size: 23px; font-weight: 700; color: var(--navy-text); line-height: 1.2; }
  .person__role { font-size: 17px; color: var(--grey-text); margin-top: 1px; }

  .divider {
    position: absolute;
    left: 50px; right: 42px; top: 249px;
    height: 1px; background: var(--rule);
  }

  .contacts {
    position: absolute; left: 48px; top: 273px;
    list-style: none;
    font-size: 15px; color: var(--grey-text);
  }
  .contacts li { display: flex; align-items: center; height: 22px; }
  .contacts svg { width: 12px; height: 12px; margin-right: 7px; fill: var(--navy-text); }

  .address {
    position: absolute; right: 42px; top: 296px;
    text-align: right; font-size: 15px; color: var(--grey-text); line-height: 22px;
  }

  .referral {
    position: absolute; left: 58px; top: 276px;
    color: var(--on-navy); font-size: 17px; line-height: 25px;
  }
  .referral strong { font-weight: 700; font-size: 24px; }
</style>
</head>
<body>
<main class="canvas">

  <section class="card card--front" aria-label="Business card front">
    <div class="brand-name">MRF ACCOUNTANTS</div>
    <p class="tagline">"The end to your tax problems begin with us"</p>

    <div class="person">
      <h1 class="person__name">Marcus Elwin</h1>
      <p class="person__role">Accountant</p>
    </div>

    <div class="divider"></div>

    <ul class="contacts">
      <li>
        <svg viewBox="0 0 12 12" aria-hidden="true"><path d="M3 1 L5 3.2 L3.8 4.6 C4.5 6.2 5.8 7.5 7.4 8.2 L8.8 7 L11 9 L9.6 11 C5 10.6 1.4 7 1 2.4 Z"/></svg>
        9481 3057
      </li>
      <li>
        <svg viewBox="0 0 12 12" aria-hidden="true"><path d="M0.5 2.5 H11.5 V9.5 H0.5 Z M1 3 L6 7 L11 3" fill="none" stroke="#0e3f78" stroke-width="1.2"/></svg>
        melwin@mrfaccountants.com.au
      </li>
      <li>
        <svg viewBox="0 0 12 12" aria-hidden="true"><g fill="none" stroke="#0e3f78" stroke-width="1.1"><circle cx="6" cy="6" r="5"/><ellipse cx="6" cy="6" rx="2.2" ry="5"/><path d="M1 6 H11 M2 3.3 H10 M2 8.7 H10"/></g></svg>
        www.mrfaccountants.com.au
      </li>
    </ul>

    <address class="address" style="font-style:normal">
      Level 5, 8 Corvale Ridge Road<br>
      ASHGROVE RISE VIC 3187
    </address>
  </section>

  <section class="card card--back" aria-label="Business card back">
    <div class="brand-name">MRF ACCOUNTANTS</div>
    <p class="referral">
      "A <strong>referral</strong> from<br>
      you is our greatest <strong>compliment"</strong>
    </p>
  </section>

</main>
</body>
</html>
```